| ▼ターゲット 10〜40代女性 健康重視な方、天然成分のサプリメントで体調管理したい方 その他6商品ほどの自社商品を出し、「お悩め解決」をテーマにしてシリーズ化を検討しております。 ▼希望デザイン方針 若くてスタイリッシュなイメージ。野菜成分仕様のため、白・緑の配色が希望 デザインイメージは添付の他社イメージを参考してください。 ▼制作依頼案 今回作っていただくのはランディングページのバナー部分となります。 今回依頼させて頂いた方にその他、同じ商品の商品紹介画像・バナー、計5〜8点のデザインをプロジェクト形式で依頼いたします。 また、今後別途依頼で別商品もお願いさせて頂く可能性があります。 ▼商品名 ブロッコリースプラウト https://www.kaimonoya-shop.jp/item/K72TQW918X/ ▼商品特徴 配合成分「ブロッコリースプラウト、明日葉、金時生姜」 スッキリする、内側からの美しさを取り入れる、自然野菜成分使用。 医薬品GMP工場で製造されたのサプリメントです。 ▼選定基準 コンセプトやイメージに沿うもの 決定後何度か修正が入る可能性がありますが、対応頂ける方。 |
皆さん素敵な提案をありがとうございました!色々迷いましたが最終的にこの提案を採用させて頂きます。理由シンプルなデザインで、弊社商品のスッキリしたイメージに適しているからです。
皆様、すばらしいご提案ありがとうございました。
今回はご縁がありませんでしたが、またの機会にお願いできればと考えております。

```html
<!DOCTYPE html>
<html lang="ja">
<head>
<meta charset="utf-8">
<title>ブロッコリースプラウト バナー</title>
<link rel="stylesheet" href="https://fonts.googleapis.com/css2?family=Noto+Sans+JP:wght@500;700;900&display=swap">
<style>
  :root {
    --bg: #ffffff;
    --ink: #1f1f1f;
    --orange: #f29a17;
    --orange-light: #f7bc2a;
    --green: #79b52b;
    --green-dark: #3d8a2a;
    --photo-skin: #e9d8cc;
    --photo-teal: #7fc9c6;
    --pack-dark: #1f3a1c;
    --pack-green: #4c7a33;
    --tablet: #5c6b34;
  }
  * { margin: 0; padding: 0; box-sizing: border-box; }
  html, body { width: 1200px; height: 372px; overflow: hidden; background: var(--bg); }
  body { font-family: "Noto Sans JP", sans-serif; color: var(--ink); }

  .banner { position: relative; width: 1200px; height: 372px; background: var(--bg); }

  .model-photo {
    position: absolute; left: 0; top: 0; width: 300px; height: 372px;
    background: linear-gradient(180deg, #f3e7de 0%, var(--photo-skin) 45%, var(--photo-teal) 100%);
  }

  .headline {
    position: absolute; left: 286px; top: 22px; width: 600px;
    text-align: center; font-weight: 900; line-height: 1;
  }
  .headline-main { font-size: 62px; letter-spacing: 2px; }
  .accent {
    background: linear-gradient(180deg, var(--orange-light), var(--orange));
    -webkit-background-clip: text; background-clip: text; color: transparent;
  }
  .headline-sub { margin-top: 22px; font-size: 44px; letter-spacing: 2px; }

  .features {
    position: absolute; left: 272px; top: 212px;
    display: flex; gap: 18px; list-style: none;
  }
  .feature {
    width: 108px; height: 108px; border-radius: 50%;
    display: flex; align-items: center; justify-content: center; text-align: center;
    color: #fff; font-weight: 700; font-size: 17px; line-height: 1.35;
    background: var(--orange);
  }
  .feature--green { background: var(--green); }
  .feature--small { font-size: 15px; }
  .feature--photo { background: radial-gradient(circle at 40% 40%, #7d8c48, var(--tablet)); }

  .product-photo {
    position: absolute; left: 915px; top: 14px; width: 175px; height: 345px;
    border-radius: 8px;
    background: linear-gradient(160deg, var(--pack-green) 0%, var(--pack-dark) 100%);
  }

  .trust-note {
    position: absolute; right: 14px; top: 20px; height: 340px;
    writing-mode: vertical-rl; color: var(--green-dark);
    font-weight: 700; font-size: 23px; line-height: 1.55; letter-spacing: 1px;
  }
</style>
</head>
<body>
  <div class="banner">
    <div class="model-photo" role="img" aria-label="笑顔でガッツポーズをするスポーツウェアの女性"></div>

    <h1 class="headline">
      <span class="headline-main"><span class="accent">内側</span>から<span class="accent">美しさ</span>を！</span>
      <span class="headline-sub" style="display:block">中からスッキリ！</span>
    </h1>

    <ul class="features">
      <li class="feature feature--green feature--small">自然野菜<br>成分使用</li>
      <li class="feature feature--small">ブロッコリー<br>スプラウト</li>
      <li class="feature">明日葉</li>
      <li class="feature">金時生姜</li>
      <li class="feature feature--photo" role="img" aria-label="緑色のサプリメント錠剤"></li>
    </ul>

    <div class="product-photo" role="img" aria-label="ブロッコリースプラウト サプリメントのパッケージ"></div>

    <p class="trust-note">医薬品GMP工場で製造された<br>安心のサプリメント</p>
  </div>
</body>
</html>
```